Postcard Design Project

Services that are meant to assist farms. Company name KELWOOD LAND SERVICES.Doing hands on work such as painting fences, Updating farm features, lawn care, rock wall restoration, farm restoration.
Updates

Target Market(s)

farm owners

Industry/Entity Type

Handyman

Colors

Designer to choose colors to be used in the design.

Requirements
Must have
• Needs to be witty and catchy to the client
Nice to have
• We want our potential clients to know that we are here to give them a hand with those projects that get left on the back burner due to time constraints.

```html
<!DOCTYPE html>
<html lang="en">
<head>
<meta charset="utf-8">
<title>Kelwood Land Services Postcard</title>
<link href="https://fonts.googleapis.com/css2?family=Roboto+Condensed:wght@700&family=Roboto:wght@300;400;700&family=Rubik:wght@700&display=swap" rel="stylesheet">
<style>
  :root{
    --stage:#1d5f8c;
    --brand-green:#39b54a;
    --ink:#111111;
    --white:#ffffff;
    --sky-top:#ffffff;
    --sky-mid:#cfe3f3;
    --sky-low:#e6f0f7;
    --grass-light:#b9dc7a;
    --grass-mid:#8cc63f;
    --grass-deep:#7bbf3a;
  }
  *{margin:0;padding:0;box-sizing:border-box}
  html,body{width:1200px;height:1200px;overflow:hidden;background:var(--stage)}
  .flyer{
    position:absolute;left:191px;top:0;width:817px;height:1200px;overflow:hidden;
    font-family:"Roboto",Arial,sans-serif;color:var(--ink);
  }
  .backdrop{
    position:absolute;inset:0;
    background:linear-gradient(to bottom,
      var(--sky-top) 0%, var(--sky-mid) 30%, var(--sky-low) 60%,
      #eef6ea 66%, var(--grass-light) 72%, var(--grass-mid) 84%, var(--grass-deep) 100%);
  }
  .band{position:absolute;top:110px;height:92px;background:var(--brand-green)}
  .band--left{left:0;width:308px}
  .band--right{left:529px;right:0}
  .band-shade{position:absolute;top:202px;height:8px;background:linear-gradient(to right,transparent,#222 80%,transparent)}
  .band-shade--left{left:130px;width:180px}
  .band-shade--right{left:529px;width:200px;background:linear-gradient(to right,#222,transparent)}
  .emblem{
    position:absolute;left:323px;top:61px;width:184px;height:184px;border-radius:50%;
    background:var(--white);display:flex;align-items:center;justify-content:center;
    font-family:"Roboto Condensed",sans-serif;font-weight:700;font-size:34px;color:var(--brand-green);
  }
  .title{
    position:absolute;left:0;right:0;top:236px;text-align:center;
    font-family:"Roboto Condensed",sans-serif;font-weight:700;font-size:84px;line-height:84px;color:var(--brand-green);
  }
  .subtitle{
    position:absolute;left:0;right:0;top:320px;text-align:center;
    font-family:"Roboto",sans-serif;font-weight:400;font-size:46px;line-height:50px;letter-spacing:0.34em;padding-left:0.34em;
  }
  .intro{
    position:absolute;left:68px;width:680px;top:384px;
    font-size:22px;line-height:29px;text-align:justify;text-align-last:left;
  }
  .service{position:absolute;display:flex;align-items:center;gap:18px}
  .service-photo{width:140px;height:140px;border-radius:50%;flex:none}
  .service-name{font-family:"Rubik",sans-serif;font-weight:700;font-size:27px;line-height:35px;text-transform:uppercase}
  .s1{left:51px;top:517px}.s1 .service-photo{background:radial-gradient(circle,#f4f6f8,#9fb1bd)}
  .s2{left:393px;top:517px}.s2 .service-photo{background:radial-gradient(circle,#7a6248,#3e5f2a)}
  .s3{left:54px;top:716px}.s3 .service-photo{background:radial-gradient(circle,#c8323b,#4f8f2c)}
  .s4{left:400px;top:716px}.s4 .service-photo{background:radial-gradient(circle,#b79d83,#6f7b55)}
  .contact-head{
    position:absolute;left:0;right:0;top:1034px;height:50px;
    display:flex;align-items:center;justify-content:center;
  }
  .rule{position:absolute;top:14px;height:16px;
    background:repeating-linear-gradient(to bottom,var(--white) 0 3px,transparent 3px 6px)}
  .rule--left{left:0;width:227px}.rule--right{left:600px;width:217px}
  .contact-label{font-weight:300;font-size:38px;line-height:44px;position:absolute;left:238px;top:0}
  .contact-line{
    position:absolute;left:74px;top:1090px;display:flex;align-items:center;gap:30px;
    font-family:"Rubik",sans-serif;font-weight:700;font-size:40px;color:var(--white);
  }
  .contact-item{display:flex;align-items:center;gap:4px}
  .at{color:var(--ink)}
</style>
</head>
<body>
  <main class="flyer">
    <div class="backdrop" role="img" aria-label="Photo of a bright sky above a close-up of green grass"></div>
    <div class="band band--left"></div>
    <div class="band band--right"></div>
    <div class="band-shade band-shade--left"></div>
    <div class="band-shade band-shade--right"></div>
    <div class="emblem">KELWOOD</div>

    <h1 class="title">KELWOOD LAND</h1>
    <p class="subtitle">SERVICES</p>

    <p class="intro">Our company is the leading company known for Contract Farming Service to the clients. We are offering these services by our experienced professionals who have complete knowledge of this field and understand the exact demands of clients.</p>

    <div class="service s1">
      <div class="service-photo" role="img" aria-label="Photo of a white picket fence"></div>
      <p class="service-name">Painting<br>Fences</p>
    </div>
    <div class="service s2">
      <div class="service-photo" role="img" aria-label="Photo of a trowel planting seedlings in soil"></div>
      <p class="service-name">Lawn Care &amp;<br>Restoration</p>
    </div>
    <div class="service s3">
      <div class="service-photo" role="img" aria-label="Photo of a red lawn mower on grass"></div>
      <p class="service-name">Updating<br>Farm<br>Features</p>
    </div>
    <div class="service s4">
      <div class="service-photo" role="img" aria-label="Photo of a stone rock wall"></div>
      <p class="service-name">Rock Wall<br>Restoration</p>
    </div>

    <div class="contact-head">
      <span class="rule rule--left"></span>
      <span class="contact-label">CONTACT US NOW</span>
      <span class="rule rule--right"></span>
    </div>
    <div class="contact-line">
      <span class="contact-item">
        <svg width="34" height="40" viewBox="0 0 24 28" aria-hidden="true"><path d="M6 1l4 1 1 6-3 2c1 4 3 8 6 10l3-2 5 3-1 5c-2 1-5 1-7-1C8 21 3 13 2 7 2 4 4 2 6 1z" fill="#111"/></svg>
        123456 789
      </span>
      <span class="contact-item"><span class="at">@</span>&nbsp;your@email.com</span>
    </div>
  </main>
</body>
</html>
```